Brightmoor Senior Living Marketing Brochure, Covid-19 Brochure, Introduction to our manager

We are a Senior Living Community that services Assisted living and memory care. We have a lot of New programs for Activities, Food recipes, therapy, family and resident interaction , covid free, and want to introduce this to the community and existing family members.

Target Market(s)

La Jolla and San Diego for Brightmoor Senior Living and Memory Care of La Jolla and For Brightmoor Senior Living and Memory Care of Tarzana , San Fernando valley, tarzana, Encino , Woodland Hills Sherman oaks

Industry/Entity Type

Assisted Living

Colors
a54499
f7f3f9
ffffff
fece3e
ffc214

Requirements
Must have
• Product names for our marketing brochure , facility images per location

```html
<!DOCTYPE html>
<html lang="en">
<head>
<meta charset="utf-8">
<title>Brightmoor Senior Living Marketing Brochure</title>
<link href="https://fonts.googleapis.com/css2?family=Fira+Sans:wght@400;500;600;700&family=Fira+Sans+Condensed:wght@600;700&family=Nunito:wght@400;600&display=swap" rel="stylesheet">
<style>
:root{
  --purple:#a54499;
  --purple-deep:#6f1f78;
  --purple-dark:#4b1566;
  --lilac:#f7f3f9;
  --white:#ffffff;
  --yellow:#fece3e;
  --gold:#ffc214;
  --ink:#1b1b1b;
  --night:#0f1416;
  --stage:#e6e3e8;
}
*{box-sizing:border-box;margin:0;padding:0}
html,body{width:1200px;height:900px;overflow:hidden;background:var(--stage)}
.stage{position:relative;width:1200px;height:900px}
.page{position:absolute;top:40px;width:580px;height:820px;overflow:hidden;background:var(--lilac);box-shadow:0 4px 18px rgba(0,0,0,.15)}
.page--front{left:12px}
.page--back{left:608px}
.layer{position:absolute;left:0;top:0}
.logo{position:absolute;font-family:"Fira Sans",sans-serif;font-weight:400;color:var(--white);font-size:31px;letter-spacing:1px}
.front-title{position:absolute;left:41px;top:104px;font-family:"Fira Sans Condensed",sans-serif;font-weight:700;color:var(--yellow);font-size:28.5px;line-height:29px}
.front-intro{position:absolute;left:41px;top:272px;width:190px;font-family:"Nunito",sans-serif;color:var(--white);font-size:8.6px;line-height:10.5px}
.tab{position:absolute;left:0;font-family:"Fira Sans",sans-serif;font-weight:700;display:flex;align-items:center}
.tab--marketing{top:411px;width:150px;height:30px;background:var(--gold);color:var(--ink);font-size:17px;padding-left:29px;border-radius:0 15px 15px 0}
.tab--salon{top:518px;width:395px;height:30px;background:var(--purple);color:var(--white);font-size:16px;padding-left:29px;border-radius:0 15px 15px 0;letter-spacing:.3px}
.marketing-copy{position:absolute;left:30px;top:446px;width:370px;font-family:"Fira Sans",sans-serif;color:var(--ink);font-size:13.6px;line-height:18.5px}
.amenities{position:absolute;left:28px;top:553px;width:375px;list-style:none;font-family:"Fira Sans",sans-serif;color:var(--ink);font-size:11px;line-height:13.6px}
.amenities li{padding-left:9px;position:relative}
.amenities li::before{content:"•";position:absolute;left:0}
.contact-band{position:absolute;left:0;width:364px;height:50px;background:var(--gold);padding-left:20px;display:flex;flex-direction:column;justify-content:center;font-family:"Fira Sans Condensed",sans-serif;font-weight:700;color:var(--ink);font-size:11.2px;line-height:15px}
.front .contact-band,.page--front .contact-band{top:718px}
.page--back .contact-band{top:711px}
.phone{position:absolute;left:20px;font-family:"Fira Sans Condensed",sans-serif;font-weight:700;font-size:30px;color:var(--ink)}
.phone span{color:var(--purple)}
.page--front .phone{top:774px}
.page--back .phone{top:768px}
.stay-home{position:absolute;left:512px;top:732px;width:56px;text-align:center;font-family:"Fira Sans Condensed",sans-serif;font-weight:600;color:var(--white);font-size:12.5px;line-height:12.8px}
.stay-home small{font-size:9px}
.features{position:absolute;left:34px;top:97px;width:320px;list-style:none;font-family:"Fira Sans",sans-serif;color:var(--white);font-size:9.3px;line-height:13.65px}
.features li{padding-left:8px;position:relative}
.features li::before{content:"•";position:absolute;left:0}
.pillar{position:absolute;top:561px;width:170px;text-align:center}
.pillar h3{font-family:"Fira Sans",sans-serif;font-weight:600;font-size:14px;line-height:16.5px;color:var(--ink)}
.pillar p{margin-top:12px;font-family:"Nunito",sans-serif;font-size:10.3px;line-height:12.4px;color:#2a2a2a}
.pillar--living{left:27px}
.pillar--connect{left:202px}
.pillar--inspire{left:377px}
.happiness-note{position:absolute;left:360px;top:738px;width:205px;text-align:right;font-family:"Nunito",sans-serif;color:var(--white);font-size:6.2px;line-height:8.2px}
</style>
</head>
<body>
<div class="stage">

  <!-- Front page -->
  <section class="page page--front">
    <svg class="layer" width="580" height="820" viewBox="0 0 580 820">
      <defs>
        <linearGradient id="frontPurple" x1="0" y1="0" x2="1" y2="1">
          <stop offset="0" stop-color="#b13a9c"/>
          <stop offset="1" stop-color="#5a1d86"/>
        </linearGradient>
        <linearGradient id="glovePhoto" x1="0" y1="0" x2="1" y2="1">
          <stop offset="0" stop-color="#1c2a2e"/>
          <stop offset=".45" stop-color="#3f8fb8"/>
          <stop offset=".75" stop-color="#6e6c6c"/>
          <stop offset="1" stop-color="#3a8fc2"/>
        </linearGradient>
        <clipPath id="frontHero">
          <path d="M0 0H580V255C520 340 430 390 300 398C160 405 60 375 0 300Z"/>
        </clipPath>
        <linearGradient id="sprayPhoto" x1="0" y1="0" x2="1" y2="1">
          <stop offset="0" stop-color="#dfe6ea"/><stop offset="1" stop-color="#8fa3ad"/>
        </linearGradient>
        <linearGradient id="carPhoto" x1="0" y1="0" x2="1" y2="1">
          <stop offset="0" stop-color="#2b3134"/><stop offset="1" stop-color="#8ea39d"/>
        </linearGradient>
        <linearGradient id="suitPhoto" x1="0" y1="0" x2="1" y2="1">
          <stop offset="0" stop-color="#e9ecef"/><stop offset="1" stop-color="#b7bcc4"/>
        </linearGradient>
      </defs>
      <rect width="580" height="820" fill="var(--lilac)"/>
      <polygon points="580,250 580,820 316,820 580,560" fill="url(#frontPurple)"/>
      <polygon points="450,430 580,300 580,820 470,820" fill="url(#frontPurple)" opacity=".85"/>
      <path d="M0 312C60 390 160 418 300 412C430 404 525 350 580 268V255C520 340 430 390 300 398C160 405 60 375 0 300Z" fill="var(--gold)"/>
      <g clip-path="url(#frontHero)">
        <rect width="580" height="420" fill="var(--night)"/>
        <rect x="230" y="40" width="350" height="370" fill="url(#glovePhoto)" role="img" aria-label="Photo of gloved hands spraying and wiping a surface clean"/>
      </g>
      <circle cx="443" cy="362" r="36" fill="var(--white)"/>
      <circle cx="443" cy="362" r="20" fill="var(--gold)"/>
      <circle cx="479" cy="483" r="84" fill="var(--gold)"/>
      <circle cx="479" cy="483" r="76" fill="url(#sprayPhoto)" role="img" aria-label="Photo of a worker in protective suit disinfecting a room"/>
      <circle cx="474" cy="642" r="70" fill="var(--gold)"/>
      <circle cx="474" cy="642" r="62" fill="url(#carPhoto)" role="img" aria-label="Photo of a vehicle interior being sanitized"/>
      <circle cx="397" cy="752" r="63" fill="var(--gold)"/>
      <circle cx="397" cy="752" r="55" fill="url(#suitPhoto)" role="img" aria-label="Photo of a worker in protective gear with a sprayer"/>
    </svg>

    <div class="logo" style="left:42px;top:50px">BRIGHTMOOR</div>
    <h1 class="front-title">Senior Living<br>Community that<br>services Assisted<br>living and<br>memory care.</h1>
    <p class="front-intro">We have a lot of New programs for Activities, Food recipes, therapy, family and resident interaction , covid free, and want to introduce this to the community and existing family members.</p>

    <div class="tab tab--marketing">MARKETING</div>
    <p class="marketing-copy">Over 125 channels included premium cable and sports. Outdoor activities including an 8 hole putting green and BBQ COURTYARD.</p>

    <div class="tab tab--salon">SALON FOR NAILS HAIR AND MASSAGES</div>
    <ul class="amenities">
      <li>Housekeeping And Laundry Services</li>
      <li>Emergency Alert System</li>
      <li>Daily Activity Schedule</li>
      <li>Beauty Salon And Barber Shop</li>
      <li>Luxury Transportation: Executive Shuttle Vans and Touring Minivans And Valet Services</li>
      <li>General Store</li>
      <li>Premium TV Package – Premium Sports Package, Movie Channels, Drama Channels And More!</li>
      <li>Movie Theatre, Shuffle Board, Pool Table And Outdoor BBQ</li>
      <li>Virtual Reality Station</li>
    </ul>

    <div class="contact-band">
      <span>4870 LINDEN CREST WAY SUITE 210 FAIRVIEW, CA 92037</span>
      <span>EMAIL: HELLO@BRIGHTMOORLIVING.NET | WEB: WWW.BRIGHTMOORLIVING.NET</span>
    </div>
    <div class="phone">PHONE: <span>858-555-0147</span></div>
    <div class="stay-home">KEEP<br>CALM<br><small>AND</small><br>STAY<br>HOME</div>
  </section>

  <!-- Back page -->
  <section class="page page--back">
    <svg class="layer" width="580" height="820" viewBox="0 0 580 820">
      <defs>
        <linearGradient id="backPurple" x1="0" y1="0" x2="0" y2="1">
          <stop offset="0" stop-color="#8a2f8c"/>
          <stop offset="1" stop-color="#6e2478"/>
        </linearGradient>
        <linearGradient id="handPhoto" x1="0" y1="0" x2="1" y2="1">
          <stop offset="0" stop-color="#39b8d8"/>
          <stop offset=".55" stop-color="#2aa3c6"/>
          <stop offset="1" stop-color="#e2409f"/>
        </linearGradient>
        <linearGradient id="backFoot" x1="0" y1="0" x2="1" y2="1">
          <stop offset="0" stop-color="#a54499"/><stop offset="1" stop-color="#6f1f78"/>
        </linearGradient>
      </defs>
      <rect width="580" height="820" fill="var(--lilac)"/>
      <path d="M0 0H580V438C480 460 380 460 290 450C170 438 80 420 0 400Z" fill="#b98fc0"/>
      <path d="M0 0H580V428C480 450 380 450 290 440C170 428 80 408 0 390Z" fill="url(#backPurple)"/>
      <path d="M300 80C330 60 400 40 440 45L520 60C560 90 580 160 580 240V420C520 430 460 410 410 380C360 340 320 300 300 250Z" fill="url(#handPhoto)" opacity=".92" role="img" aria-label="Photo of pink gloved hands holding a blue hand sanitizer bottle"/>
      <g fill="var(--white)">
        <circle cx="112" cy="510" r="40"/><circle cx="287" cy="510" r="40"/><circle cx="462" cy="510" r="40"/>
      </g>
      <g fill="var(--gold)">
        <circle cx="112" cy="510" r="35"/><circle cx="287" cy="510" r="35"/><circle cx="462" cy="510" r="35"/>
      </g>
      <g fill="none" stroke="var(--ink)" stroke-width="3.5" stroke-linecap="round" stroke-linejoin="round">
        <path d="M96 512L112 496L128 512M100 510V528H124V510"/>
        <path d="M279 518L273 524a6 6 0 0 1-8-8l8-8a6 6 0 0 1 8 0M295 502l6-6a6 6 0 0 1 8 8l-8 8a6 6 0 0 1-8 0M281 516l12-12"/>
        <path d="M455 520a11 11 0 1 1 14 0V526H455ZM457 530H467M462 483V488M446 490L449 493M478 490L475 493M442 504H446M482 504H478"/>
      </g>
      <polygon points="364,711 580,711 580,820 311,820" fill="url(#backFoot)"/>
    </svg>

    <div class="logo" style="left:38px;top:24px">BRIGHTMOOR</div>
    <ul class="features">
      <li>Multiple Resident Assessments based on Service Types</li>
      <li>Resident Task Scheduling and Service Plans</li>
      <li>End of Shift Reporting</li>
      <li>Resident Care Threads</li>
      <li>Resident Focus Areas and Incident Tracking and Reporting</li>
      <li>Meaningful and Customizable Dashboards</li>
      <li>Availability of standardized Focus Areas and Follow up Protocols</li>
      <li>Cost of Care Variance Reporting</li>
      <li>customized Assessments (based on flexible points, time, or flat rate)</li>
      <li>eMAR</li>
      <li>Acuity Analysis</li>
      <li>State Forms and Reporting</li>
      <li>Scheduled care (includes non-assessment related tasks such asphysician visits, TB testing, etc.)</li>
      <li>Acuity levels</li>
      <li>Staffing needs analysis for your Assisted Living, Memory Care or CCRC community is based on up-to-date resident assessments.</li>
      <li>Document resident risks, past incidents, individual behaviors, preferences, and additional family and caregiver input.</li>
      <li>Family and Resident Portal</li>
      <li>Brightmoor Senior Living is overcoming social isolation through the power of virtual reality and shared experiences.</li>
    </ul>

    <div class="pillar pillar--living">
      <h3>Living<br>Relive</h3>
      <p>Customized reminiscence therapy tools allow your residents to take a stroll down memory lane by revisiting their childhood home, wedding location or anywhere else from their past.</p>
    </div>
    <div class="pillar pillar--connect">
      <h3>Connect<br>Reconnect</h3>
      <p>Provide opportunities for your loved ones to virtually leave the four walls of our community to check off bucket list itemsand engage with the world in ways they never thought possible.</p>
    </div>
    <div class="pillar pillar--inspire">
      <h3>Lightbulb<br>Reinspire</h3>
      <p>Create new friendships through the power of shared experience, all while providing unforgettable moments and stories that residents and their families will remember forever.</p>
    </div>

    <div class="contact-band">
      <span>4870 LINDEN CREST WAY SUITE 210 FAIRVIEW, CA 92037</span>
      <span>EMAIL: HELLO@BRIGHTMOORLIVING.NET | WEB: WWW.BRIGHTMOORLIVING.NET</span>
    </div>
    <div class="phone">PHONE: <span>858-555-0147</span></div>
    <p class="happiness-note">Bar chart bars Bar chart dotsOur communities have shown a 40% increase in resident happiness Brightmoor Senior Living gives during this Pandemic a window to the parts of the world that they're missing.Family Family Members Normally, you can't control how much stimulation your loved one experiences everyday. You can trust that a our community thinks of resident happiness first.</p>
  </section>

</div>
</body>
</html>
```